Business Card Makeover. Recreate a sleek modern design for our business card.

DO NOT COPY OUR CURRENT DESIGN. MUST BE ONE SIDED BUSINESS CARD.
Create a new business card design, using our new logo. Attached is a sample of our current design and new logo. Please note the address and email will change. The new address is 417 Corvell West Palm Beach 33472 and our website will be www.talvendrake.example.

We are an architectural and interior design firm. We prefer a clean modern look. Something that is refined and emulates excellence.

Industry/Entity Type

Architecture

Contact Information for Business Card

clean modern look, please do not copy our attached design.

Font styles to use
Other font styles liked:
• see attached business card font

Colors

Designer to choose colors to be used in the design.

Requirements
Must have
• Must have a modern appeal and resemble our current branding.
Nice to have
• modern font, our logo, legible name and titles progressive design
Should not have
• Do not add colors not reflected in our branding. Should not look like our current card.

```html
<!DOCTYPE html>
<html lang="en">
<head>
<meta charset="utf-8">
<title>Talvendrake + Partners — Business Card</title>
<link rel="stylesheet" href="https://fonts.googleapis.com/css2?family=Open+Sans:wght@400;700;800&family=Arimo:wght@400&display=swap">
<style>
  :root {
    --brand-blue: #0f4aa0;
    --ink: #111111;
    --ink-soft: #333333;
    --card: #ffffff;
    --backdrop: #e9e9ec;
  }
  html, body {
    margin: 0;
    width: 1200px;
    height: 1023px;
    overflow: hidden;
    background: var(--backdrop);
  }
  .card {
    position: absolute;
    left: 150px;
    top: 254px;
    width: 900px;
    height: 514px;
    background: var(--card);
    overflow: hidden;
    box-shadow: 0 6px 24px rgba(0,0,0,0.12);
    font-family: "Arimo", Arial, sans-serif;
    color: var(--ink);
  }
  .crescent {
    position: absolute;
    inset: 0;
  }
  .name {
    position: absolute;
    left: 58px;
    top: 52px;
    margin: 0;
    font-family: "Open Sans", Arial, sans-serif;
    font-weight: 800;
    color: var(--brand-blue);
    font-size: 48px;
    line-height: 50px;
    letter-spacing: 1px;
  }
  .name .credentials {
    font-weight: 700;
    font-size: 32px;
    letter-spacing: 1px;
  }
  .name .credentials sup {
    font-size: 14px;
    font-weight: 400;
    vertical-align: 14px;
  }
  .title {
    position: absolute;
    left: 60px;
    top: 160px;
    margin: 0;
    font-size: 25px;
    letter-spacing: 0.5px;
    color: var(--ink);
  }
  .brand {
    position: absolute;
    left: 300px;
    top: 40px;
    display: flex;
    align-items: center;
    gap: 12px;
  }
  .brand-dot {
    width: 30px;
    height: 30px;
    border-radius: 50%;
    background: var(--brand-blue);
  }
  .brand-name {
    font-family: "Open Sans", Arial, sans-serif;
    font-weight: 400;
    font-size: 22px;
    letter-spacing: 1.5px;
    color: var(--ink-soft);
  }
  .services {
    position: absolute;
    left: 714px;
    top: 214px;
    margin: 0;
    font-family: "Open Sans", Arial, sans-serif;
    font-weight: 700;
    font-size: 13px;
    line-height: 20px;
    letter-spacing: 2px;
    color: var(--brand-blue);
  }
  .phones {
    position: absolute;
    left: 420px;
    top: 300px;
    font-size: 17px;
    line-height: 22px;
  }
  .phones .license {
    color: var(--brand-blue);
    margin-bottom: 8px;
  }
  .address {
    position: absolute;
    left: 230px;
    top: 372px;
    font-size: 17px;
    line-height: 22px;
    color: var(--ink-soft);
  }
  .address .web {
    margin-top: 22px;
    color: var(--ink);
  }
</style>
</head>
<body>
  <main class="card">
    <svg class="crescent" width="900" height="514" viewBox="0 0 900 514" aria-hidden="true">
      <circle cx="870" cy="230" r="250" fill="var(--brand-blue)"/>
      <circle cx="900" cy="250" r="205" fill="var(--card)"/>
    </svg>

    <h1 class="name">MARISA<br>DELCOURT<span class="credentials">, AIA, LEED<sup>®</sup> AP</span></h1>
    <p class="title">PARTNER, PROJECT ARCHITECT</p>

    <div class="brand">
      <span class="brand-dot"></span>
      <span class="brand-name">TALVENDRAKE + PARTNERS</span>
    </div>

    <p class="services">ARCHITECTURE<br>INTERIOR DESIGN</p>

    <div class="phones">
      <div class="license">LIC.# AA51730842</div>
      <div>office: 561.555.0144</div>
      <div>fax: 561.555.0178</div>
    </div>

    <div class="address">
      <div>417 Corvell</div>
      <div>West Palm Beach 33472</div>
      <div class="web">marisa@talvendrake.example</div>
      <div>www.talvendrake.example</div>
    </div>
  </main>
</body>
</html>
```